VoyaPoint

1. We need a four color business card
2. The Front of card needs to include our Logo, Slogan which is "Launching, Expanding & Optimizing Organizations, Individual Name, email, two phone numbers, email, skype address, website address
3. Back of card needs to include the following topics: Start Ups & Business Optimization,Product Acquisition, Destination Product Marketing & Representation,Marketing & Sales, Operations, Training/Education, Digital Marketing, Keynote Addresses/Public Speaking
3. Back of card can not be black as it needs to be a color that people can write on
Industry/Entity Type
Business

```html
<!DOCTYPE html>
<html lang="en">
<head>
<meta charset="utf-8">
<title>VoyaPoint Business Card</title>
<link href="https://fonts.googleapis.com/css2?family=Varela+Round&display=swap" rel="stylesheet">
<style>
  :root {
    --page-bg: #d9dbde;
    --card-bg: #ffffff;
    --brand-blue: #1f6fc9;
    --brand-green: #8cb82b;
    --brand-orange: #f26a1b;
    --ink-grey: #5a5f66;
    --accent-faint: #e7edf3;
  }
  * { margin: 0; padding: 0; box-sizing: border-box; }
  html, body {
    width: 1200px;
    height: 900px;
    overflow: hidden;
    background: var(--page-bg);
    font-family: "Varela Round", Arial, sans-serif;
  }
  .sheet {
    position: relative;
    width: 1200px;
    height: 900px;
  }
  .card {
    position: absolute;
    top: 295px;
    width: 540px;
    height: 310px;
    background: var(--card-bg);
    border-radius: 4px;
    box-shadow: 0 10px 30px rgba(0,0,0,0.18);
    overflow: hidden;
  }
  .card--front { left: 40px; }
  .card--back { left: 620px; }

  .brand {
    position: absolute;
    top: 22px;
    left: 24px;
    display: flex;
    align-items: center;
    gap: 10px;
  }
  .brand__dot {
    width: 30px;
    height: 30px;
    border-radius: 50%;
    background: var(--brand-blue);
  }
  .brand__name {
    font-size: 30px;
    color: var(--ink-grey);
    letter-spacing: 0.5px;
  }
  .slogan {
    position: absolute;
    top: 68px;
    left: 24px;
    font-size: 13px;
    color: var(--brand-blue);
  }
  .backdrop-circle {
    position: absolute;
    left: 20px;
    top: 110px;
    width: 190px;
    height: 190px;
    border-radius: 50%;
    background: var(--accent-faint);
  }

  .contact {
    position: absolute;
    right: 30px;
    top: 108px;
    text-align: right;
    line-height: 1.4;
  }
  .contact__name { font-size: 24px; color: var(--brand-orange); }
  .contact__email { font-size: 19px; color: var(--brand-green); }
  .contact__phone { font-size: 19px; color: var(--brand-blue); }

  .footer-band {
    position: absolute;
    left: 0;
    right: 0;
    bottom: 0;
    height: 46px;
  }
  .footer-band__web {
    position: absolute;
    left: 0; bottom: 0;
    width: 55%;
    height: 34px;
    background: var(--brand-blue);
    color: #fff;
    font-size: 14px;
    padding: 9px 0 0 60px;
  }
  .footer-band__mark {
    position: absolute;
    left: 55%; bottom: 0;
    width: 5%;
    height: 34px;
    background: var(--brand-orange);
  }
  .footer-band__skype {
    position: absolute;
    left: 60%; bottom: 0;
    width: 40%;
    height: 46px;
    background: var(--brand-green);
    color: #fff;
    font-size: 14px;
    padding: 14px 0 0 80px;
  }

  .services {
    position: absolute;
    right: 28px;
    top: 96px;
    list-style: none;
    text-align: right;
    font-size: 15px;
    line-height: 1.55;
  }
  .services li:nth-child(odd) { color: var(--brand-blue); }
  .services li:nth-child(even) { color: var(--brand-green); }
</style>
</head>
<body>
<main class="sheet">
  <section class="card card--front" aria-label="Card front">
    <div class="backdrop-circle"></div>
    <div class="brand">
      <span class="brand__dot"></span>
      <span class="brand__name">VoyaPoint</span>
    </div>
    <p class="slogan">Launching, Expanding &amp; Optimizing Organizations.</p>
    <div class="contact">
      <p class="contact__name">John Doe.</p>
      <p class="contact__email">johnd@voyapoint.com.</p>
      <p class="contact__phone">555-5555/555-5554.</p>
    </div>
    <div class="footer-band">
      <div class="footer-band__web">website address</div>
      <div class="footer-band__mark"></div>
      <div class="footer-band__skype">skype address</div>
    </div>
  </section>

  <section class="card card--back" aria-label="Card back">
    <div class="backdrop-circle"></div>
    <div class="brand">
      <span class="brand__dot"></span>
      <span class="brand__name">VoyaPoint</span>
    </div>
    <p class="slogan">Launching, Expanding &amp; Optimizing Organizations.</p>
    <ul class="services">
      <li>Start Ups &amp; Business Optimization.</li>
      <li>Product Acquisition.</li>
      <li>Destination Product</li>
      <li>Marketing &amp; Representation.</li>
      <li>Marketing &amp; Sales, Operations.</li>
      <li>Training/Education, Digital Marketing.</li>
      <li>Keynote Addresses/Public Speaking</li>
    </ul>
  </section>
</main>
</body>
</html>
```